The Hollow Orchard ebook cover for Corwin Ashby Pellegrew

I need an ebook cover/jpeg that depicts a Middle-Eastern desert and sky. The cover must be very elegant and very austere, the simpler the better.
Toward the top, the text will read: The Hollow Orchard
Directly below the title will read: Bertil Quennoch
The dimensions for the cover should be 2560 pixels (height) and 1600 pixels (width.)

Target Market(s)

Readers of serious magical realism and/or fantasy literature with a serious literary element.

Font styles to use
Serif

Requirements
Must have
• My ebook cover MUST be a painting or illustration depicting a very austere Middle-Eastern desert and desert sky. Must be elegant and austere. The lettering of the title and author name must blend in beautifully with the image--just like fine books in a bookstore. Title must appear at the top: The Hollow Orchard. The author's name must appear below title and read: Bertil Quennoch. Dimensions must be 2560 pixels (height) by 1600 pixels (width)
Nice to have
• A very austere desert on the bottom and a sad elegant sky above.
Should not have
• My ebook cover should not have a spine or a back. I just need an ebook cover of the dimensions stated above.

```html
<!DOCTYPE html>
<html lang="en">
<head>
<meta charset="utf-8">
<title>The Hollow Orchard — Ebook Cover</title>
<link href="https://fonts.googleapis.com/css2?family=Cinzel:wght@400;500&display=swap" rel="stylesheet">
<style>
  :root {
    --stage: #8f8e8f;
    --sky-top: #8fb5e2;
    --sky-low: #b4d4f0;
    --dune-shadow: #1c1308;
    --dune-glow: #f29b22;
    --dune-deep: #d47510;
    --ink: #111111;
    --title-red: #a3000a;
  }
  html, body {
    margin: 0;
    padding: 0;
    width: 1200px;
    height: 996px;
    overflow: hidden;
    background: var(--stage);
  }
  .cover {
    position: absolute;
    left: 306px;
    top: 28px;
    width: 588px;
    height: 940px;
    overflow: hidden;
    box-shadow: 0 4px 14px rgba(0,0,0,0.35);
  }
  .cover__artwork {
    position: absolute;
    inset: 0;
    background: linear-gradient(
      to bottom,
      var(--sky-top) 0%,
      var(--sky-low) 39%,
      var(--dune-shadow) 41%,
      var(--dune-shadow) 46%,
      var(--dune-deep) 52%,
      var(--dune-glow) 66%,
      var(--dune-deep) 80%,
      var(--dune-shadow) 92%,
      var(--dune-shadow) 100%
    );
  }
  .cover__titles {
    position: absolute;
    left: 0;
    right: 0;
    top: 120px;
    text-align: center;
    font-family: "Cinzel", serif;
  }
  .title__lead {
    margin: 0;
    font-size: 46px;
    font-weight: 400;
    letter-spacing: 5px;
    color: var(--ink);
    line-height: 1;
  }
  .title__main {
    margin: 2px 0 0;
    font-size: 92px;
    font-weight: 500;
    letter-spacing: 1px;
    color: var(--title-red);
    line-height: 1;
  }
  .cover__author {
    margin: 44px 0 0;
    font-size: 24px;
    font-weight: 400;
    letter-spacing: 3px;
    color: var(--ink);
  }
</style>
</head>
<body>
  <main class="cover">
    <div class="cover__artwork" role="img" aria-label="Photograph of austere desert dunes in deep orange light and black shadow beneath a pale blue sky"></div>
    <header class="cover__titles">
      <h1 class="title">
        <span class="title__lead" style="display:block">The Hollow</span>
        <span class="title__main" style="display:block">ORCHARD</span>
      </h1>
      <p class="cover__author">Bertil Quennoch</p>
    </header>
  </main>
</body>
</html>
```